Business card for exciting VC company

Should look simple, crisp, and modern.

Industry/Entity Type

Venture Capital

Contact Information for Business Card

Would like to see at least one design that has our blue on the back with the tagline "Reshaping Established Markets" and white front with contact details.

Font styles to use
Sans Serif

Requirements
Must have
• Logo

Gregory Tallis
gtallis@brindlewave.vc
Managing Partner
M (628)354-xxxx

```html
<!DOCTYPE html>
<html lang="en">
<head>
<meta charset="UTF-8">
<title>Brindlewave Capital — Business Card</title>
<link rel="stylesheet" href="https://fonts.googleapis.com/css2?family=Montserrat:wght@400;500;600&display=swap">
<style>
  :root {
    --backdrop-inner: #323232;
    --backdrop-outer: #141414;
    --brand-blue: #4585c8;
    --brand-blue-light: #5a95d0;
    --card-dark: #191919;
    --card-dark-edge: #262626;
    --ink-white: #ffffff;
    --ink-soft: #e9e9e9;
    --rule-grey: #8a8a8a;
  }
  * { box-sizing: border-box; margin: 0; padding: 0; }
  html, body {
    width: 1200px;
    height: 900px;
    overflow: hidden;
  }
  body {
    background: radial-gradient(ellipse at 65% 40%, var(--backdrop-inner), var(--backdrop-outer) 75%);
    font-family: "Montserrat", sans-serif;
    position: relative;
  }
  .card {
    position: absolute;
    left: 320px;
    width: 560px;
    height: 320px;
    box-shadow: 0 18px 40px rgba(0, 0, 0, 0.55);
  }
  .card--back {
    top: 80px;
    background: linear-gradient(100deg, var(--brand-blue) 55%, var(--brand-blue-light));
    display: flex;
    flex-direction: column;
    align-items: center;
    justify-content: center;
  }
  .card--front {
    top: 480px;
    background: linear-gradient(110deg, var(--card-dark) 50%, var(--card-dark-edge));
    border-bottom: 6px solid var(--brand-blue);
    display: flex;
    align-items: center;
    padding: 0 30px 0 40px;
  }
  .wordmark {
    display: flex;
    align-items: center;
    gap: 12px;
    color: var(--ink-white);
    font-weight: 500;
  }
  .wordmark__square {
    width: 14px;
    height: 14px;
    background: var(--ink-white);
    flex: none;
  }
  .wordmark__text {
    display: flex;
    flex-direction: column;
    line-height: 1.1;
  }
  .wordmark__name {
    font-size: 32px;
    letter-spacing: 3px;
  }
  .wordmark__sub {
    font-size: 13px;
    letter-spacing: 8px;
    margin-top: 4px;
  }
  .card--back .wordmark { margin-top: 10px; }
  .tagline {
    position: absolute;
    bottom: 28px;
    left: 0;
    right: 0;
    text-align: center;
    color: var(--ink-white);
    font-size: 12.5px;
    letter-spacing: 1.6px;
    font-weight: 400;
  }
  .card--front .wordmark__name { font-size: 23px; letter-spacing: 2px; }
  .card--front .wordmark__sub { font-size: 10.5px; letter-spacing: 6px; }
  .card--front .wordmark__square { width: 11px; height: 11px; }
  .divider {
    width: 1px;
    height: 110px;
    background: var(--rule-grey);
    margin: 0 20px;
    flex: none;
  }
  .contact { color: var(--ink-soft); }
  .contact__name {
    color: var(--brand-blue);
    font-weight: 600;
    font-size: 19px;
    letter-spacing: 0.5px;
    text-transform: uppercase;
  }
  .contact__role {
    font-size: 13.5px;
    margin-top: 2px;
    margin-bottom: 16px;
  }
  .contact__line {
    display: flex;
    align-items: center;
    gap: 9px;
    font-size: 14px;
    margin-top: 8px;
  }
  .contact__icon { width: 12px; height: 12px; flex: none; }
</style>
</head>
<body>
  <section class="card card--back">
    <div class="wordmark">
      <span class="wordmark__square"></span>
      <div class="wordmark__text">
        <span class="wordmark__name">BRINDLEWAVE</span>
        <span class="wordmark__sub">CAPITAL</span>
      </div>
    </div>
    <p class="tagline">RESHAPING ESTABLISHED MARKETS</p>
  </section>

  <section class="card card--front">
    <div class="wordmark">
      <span class="wordmark__square"></span>
      <div class="wordmark__text">
        <span class="wordmark__name">BRINDLEWAVE</span>
        <span class="wordmark__sub">CAPITAL</span>
      </div>
    </div>
    <span class="divider"></span>
    <div class="contact">
      <p class="contact__name">Gregory Tallis</p>
      <p class="contact__role">Managing Partner</p>
      <p class="contact__line">
        <svg class="contact__icon" viewBox="0 0 24 24" aria-hidden="true">
          <path fill="#4585c8" d="M6.6 10.8a15.1 15.1 0 0 0 6.6 6.6l2.2-2.2c.3-.3.7-.4 1-.2 1.1.4 2.3.6 3.6.6.6 0 1 .4 1 1V20c0 .6-.4 1-1 1A17 17 0 0 1 3 4c0-.6.4-1 1-1h3.5c.6 0 1 .4 1 1 0 1.3.2 2.5.6 3.6.1.3 0 .7-.2 1z"/>
        </svg>
        (628)354-xxxx
      </p>
      <p class="contact__line">
        <svg class="contact__icon" viewBox="0 0 24 24" aria-hidden="true">
          <path fill="#4585c8" d="M2 5h20v14H2z"/>
          <path fill="none" stroke="#191919" stroke-width="1.6" d="M2 5l10 8 10-8"/>
        </svg>
        gtallis@brindlewave.vc
      </p>
    </div>
  </section>
</body>
</html>
```